Business Card Design

I would like a new business card design for an accounting firm that specializes in resolving clients tax problems. I want the card to give the impression that we are not your typical stodgy accounting firm, but at the same time we will get the job done.
Industry/Entity Type
Business
Contact Information for Business Card
Marcus T Kelbeck
Certified Public Accountant
27-08 63rd Avenue
Fernbrook, NY 11398
Tel: (718) 555-0143
Fax: (888) 555-0176
e-mail: mtkledger@quillpost.net
website: harborstonefiscalaidgroup.com

```html
<!DOCTYPE html>
<html lang="en">
<head>
<meta charset="utf-8">
<title>Marcus T Kelbeck – Business Card</title>
<link href="https://fonts.googleapis.com/css2?family=Open+Sans:ital,wght@0,400;0,600;1,400&display=swap" rel="stylesheet">
<style>
  :root {
    --navy: #17406f;
    --gold: #f5c518;
    --white: #ffffff;
    --backdrop: #e4e5e7;
  }
  html, body {
    margin: 0;
    width: 1200px;
    height: 1200px;
    overflow: hidden;
    background: var(--backdrop);
    font-family: "Open Sans", Arial, sans-serif;
  }
  .card {
    position: absolute;
    left: 60px;
    top: 291px;
    width: 1080px;
    height: 617px;
    background: var(--navy);
    overflow: hidden;
  }
  .card-shapes {
    position: absolute;
    inset: 0;
    width: 100%;
    height: 100%;
  }
  .brand {
    position: absolute;
    left: 60px;
    top: 150px;
    width: 470px;
    display: flex;
    align-items: center;
    gap: 16px;
  }
  .brand-dot {
    width: 30px;
    height: 30px;
    border-radius: 50%;
    background: var(--gold);
    flex: none;
  }
  .brand-name {
    color: var(--navy);
    font-weight: 600;
    font-size: 40px;
    line-height: 1;
    white-space: nowrap;
  }
  .identity {
    position: absolute;
    left: 660px;
    top: 98px;
    color: var(--white);
  }
  .identity-name {
    margin: 0;
    font-size: 41px;
    font-weight: 600;
    line-height: 1.1;
  }
  .identity-title {
    margin: 4px 0 0;
    font-size: 22px;
    font-style: italic;
    line-height: 1.2;
  }
  .contacts {
    position: absolute;
    left: 672px;
    top: 0;
    margin: 0;
    padding: 0;
    list-style: none;
    color: var(--white);
    font-size: 22px;
    line-height: 1.4;
  }
  .contact {
    position: absolute;
    left: 0;
    display: flex;
    align-items: center;
    gap: 14px;
    white-space: nowrap;
    transform: translateY(-50%);
  }
  .contact svg {
    width: 34px;
    height: 34px;
    flex: none;
    fill: var(--white);
  }
  .contact--phone { top: 270px; }
  .contact--fax { top: 325px; }
  .contact--address { top: 388px; }
  .contact--email { top: 454px; }
  .contact--web { top: 505px; }
</style>
</head>
<body>
  <main class="card">
    <svg class="card-shapes" viewBox="0 0 735 420" preserveAspectRatio="none" aria-hidden="true">
      <path fill="var(--white)" d="M0,0 H407 C432,120 400,300 235,362 C155,386 70,380 0,373 Z"/>
      <path fill="var(--gold)" d="M396,148 C394,240 335,308 248,332 C322,290 378,230 396,148 Z"/>
    </svg>

    <div class="brand">
      <span class="brand-dot"></span>
      <span class="brand-name">Marcus T Kelbeck</span>
    </div>

    <header class="identity">
      <h1 class="identity-name">Marcus T Kelbeck</h1>
      <p class="identity-title">Certified Public Accountant</p>
    </header>

    <ul class="contacts">
      <li class="contact contact--phone">
        <svg viewBox="0 0 24 24" aria-hidden="true"><path d="M6.6 10.8c1.4 2.8 3.8 5.1 6.6 6.6l2.2-2.2c.3-.3.7-.4 1-.2 1.1.4 2.3.6 3.6.6.6 0 1 .4 1 1V20c0 .6-.4 1-1 1C10.6 21 3 13.4 3 4c0-.6.4-1 1-1h3.5c.6 0 1 .4 1 1 0 1.3.2 2.5.6 3.6.1.3 0 .7-.2 1z M14 3a7 7 0 0 1 7 7h-1.6A5.4 5.4 0 0 0 14 4.6z M14 6.4a3.6 3.6 0 0 1 3.6 3.6H16A2 2 0 0 0 14 8z"/></svg>
        <span>(718) 555-0143</span>
      </li>
      <li class="contact contact--fax">
        <svg viewBox="0 0 24 24" aria-hidden="true"><path d="M7 2h10v7H7z M3 10h18v11H3z M8 14v3h8v-3z" fill-rule="evenodd"/></svg>
        <span>(888) 555-0176</span>
      </li>
      <li class="contact contact--address">
        <svg viewBox="0 0 24 24" aria-hidden="true"><path fill-rule="evenodd" d="M12 2a7 7 0 0 1 7 7c0 5-7 13-7 13S5 14 5 9a7 7 0 0 1 7-7zm0 4.3a2.7 2.7 0 1 0 0 5.4 2.7 2.7 0 0 0 0-5.4z"/></svg>
        <span>27-08 63rd Avenue<br>Fernbrook, NY 11398</span>
      </li>
      <li class="contact contact--email">
        <svg viewBox="0 0 24 24" aria-hidden="true"><path d="M12 3l9 6v11H3V9z M5 10l7 5 7-5-7-4.6z" fill-rule="evenodd"/></svg>
        <span>mtkledger@quillpost.net</span>
      </li>
      <li class="contact contact--web">
        <svg viewBox="0 0 24 24" aria-hidden="true"><path fill="none" stroke="var(--white)" stroke-width="1.6" d="M12 3a9 9 0 1 0 0 18 9 9 0 0 0 0-18z M3 12h18 M12 3c-3 3-3 15 0 18 M12 3c3 3 3 15 0 18 M5 7h14 M5 17h14"/></svg>
        <span>harborstonefiscalaidgroup.com</span>
      </li>
    </ul>
  </main>
</body>
</html>
```